Podiatry clinic requires a modern revamp and editing of existing website.

I would like a fresh new look and updated information for my current business website. An easy to navigate site with prominent address and phone number for call to action. We are a podiatry clinic that focuses on general and sports podiatry.
I would like 4 pages; including Home page, About Us, Services & Contact.
www.brambleridgefootcare.com

Target Market(s)

Active working professionals.

Industry/Entity Type

Medical

Coding

Coded - Design and coding required

Number of Pages Required

4 page

Font styles to use
Sans Serif

Colors
6b449b

Requirements
Must have
• A modern look with logo and active images; clean and uncluttered. Visible phone number and address for call to action.
• 4 pages - Home, About Us, Services, Contact.
• Home page - update address & service logos.
• About Us - update of personal information.
• Services - Revamp of existing page.
• Contact page to include Google map, email & phone number.
Nice to have
• Ability to add content easily; eg. a blog or adding video onto Home page.
• Link to Facebook page.

```html
<!DOCTYPE html>
<html lang="en">
<head>
<meta charset="utf-8">
<title>Bramble Ridge Foot Care</title>
<link href="https://fonts.googleapis.com/css2?family=Hind:wght@400;500;600;700&family=Open+Sans:wght@400;600;700&display=swap" rel="stylesheet">
<style>
:root{
  --purple:#5a3f86;
  --purple-mid:#6b449b;
  --purple-bright:#4f36a6;
  --lilac:#8a74bd;
  --lilac-text:#9c86cf;
  --dark:#1c1c1e;
  --nav:#262626;
  --ink:#333;
  --muted:#666;
  --page:#eef3f7;
  --frame:#e6e6e6;
  --white:#fff;
}
*{margin:0;padding:0;box-sizing:border-box}
html,body{width:931px;height:1200px;overflow:hidden;background:var(--frame)}
body{font-family:"Open Sans",sans-serif;color:var(--ink);position:relative}
.site{position:absolute;left:10px;top:10px;width:910px;height:1180px;background:var(--page);overflow:hidden}
.abs{position:absolute}

/* header */
.header{left:0;top:0;width:910px;height:94px;background:var(--purple)}
.logo-box{left:19px;top:0;width:193px;height:112px;background:var(--lilac);box-shadow:0 2px 4px rgba(0,0,0,.25);display:flex;align-items:center;gap:8px;padding:0 16px;z-index:3}
.logo-dot{width:14px;height:14px;border-radius:50%;background:var(--white);flex:none}
.logo-name{font-family:"Hind",sans-serif;font-weight:700;font-size:19px;line-height:21px;color:var(--white)}
.top-tab{left:574px;top:0;width:324px;height:30px;background:#7b66ac;clip-path:polygon(0 0,100% 0,94% 100%,6% 100%);display:flex;align-items:center;justify-content:center;gap:8px;font-family:"Hind",sans-serif;font-weight:600;font-size:12px;color:var(--white)}
.circle-icon{width:14px;height:14px;border:1.5px solid var(--white);border-radius:50%;display:inline-block}
.contact-row{left:428px;top:54px;display:flex;gap:26px;font-family:"Hind",sans-serif;font-weight:600;font-size:14.5px;color:var(--white);align-items:center}
.contact-row span{display:flex;align-items:center;gap:7px}

/* nav */
.nav{left:0;top:94px;width:910px;height:36px;background:var(--nav)}
.nav a{position:absolute;top:10px;font-family:"Hind",sans-serif;font-weight:600;font-size:13px;color:var(--white);text-decoration:none;letter-spacing:.2px}
.nav a.active{color:#b9a9e4}
.nav a.active::after{content:"";position:absolute;left:50%;bottom:-12px;margin-left:-5px;border:5px solid transparent;border-bottom-color:#b9a9e4}

/* hero */
.hero-panel{top:130px;height:394px}
.p1{left:0;width:228px;background:linear-gradient(135deg,#3d4654,#7a5a3c 55%,#2a2d33)}
.p2{left:228px;width:227px;background:linear-gradient(180deg,#8e99a6,#2b2b30 45%,#6d7075)}
.p3{left:455px;width:181px;background:linear-gradient(180deg,#c9b184,#54463a 50%,#2f2a27)}
.p4{left:636px;width:274px;background:linear-gradient(180deg,#6d4530,#a56a48 50%,#4a3024)}

.services-card{left:636px;top:148px;width:201px;height:376px;background:var(--white);border-radius:8px 8px 0 0}
.services-title{position:absolute;left:0;top:8px;width:201px;text-align:center;font-family:"Hind",sans-serif;font-weight:700;font-size:14px;color:var(--purple-mid)}
.treat-band{left:622px;top:180px;width:230px;height:20px;background:var(--purple-bright);color:var(--white);font-family:"Hind",sans-serif;font-weight:600;font-size:12px;text-align:center;line-height:21px}
.treat-photo{left:622px;top:200px;width:230px;height:66px;background:linear-gradient(135deg,#8fa4c3,#e7e9ee 50%,#9aa6bd)}
.card-text{position:absolute;left:12px;width:177px;text-align:center;font-size:9.2px;line-height:13px;color:var(--muted)}
.card-divider{position:absolute;left:0;top:247px;width:201px;height:1px;background:#ddd}
.card-head{font-family:"Hind",sans-serif;font-weight:600;font-size:12px;color:#222;margin-bottom:1px}

/* welcome */
.welcome-title{left:76px;top:570px;font-family:"Hind",sans-serif;font-weight:700;font-size:23px;color:#222}
.welcome-title span{color:var(--lilac-text)}
.rule{top:624px;height:1px;background:#c9ced4}
.rule-dot{left:273px;top:618px;width:10px;height:14px;border-radius:50%;background:var(--purple-bright)}
.intro{left:45px;top:662px;width:470px;font-size:11.2px;line-height:15px;color:#333}
.intro p{margin-bottom:14px}
.intro b{color:var(--purple-bright);font-weight:600}
.btn{top:850px;height:31px;background:var(--purple-bright);color:var(--white);font-family:"Hind",sans-serif;font-weight:700;font-size:13.5px;display:flex;align-items:center;gap:10px;padding-left:12px;clip-path:polygon(0 0,94% 0,100% 50%,94% 100%,0 100%);border-bottom:2px solid #3a2786}
.btn-services{left:44px;width:200px}
.btn-videos{left:255px;width:201px}

/* appointment */
.form-shell{left:606px;top:566px;width:262px;height:320px;background:var(--white);box-shadow:0 10px 12px -8px rgba(0,0,0,.3)}
.form-cap{left:616px;top:566px;width:244px;height:19px;background:#e3e3e3}
.form-head{left:606px;top:585px;width:262px;height:35px;background:var(--purple-bright);color:var(--white);font-family:"Hind",sans-serif;font-weight:600;font-size:15px;text-align:center;line-height:37px}
.field-icon{left:630px;width:26px;height:25px;border:1px solid #ddd;background:#f4f4f4;display:flex;align-items:center;justify-content:center}
.field{left:658px;width:186px;height:25px;border:1px solid #ddd;background:#f7f7f7;font-family:"Hind",sans-serif;font-weight:500;font-size:10px;color:#333;padding:7px 0 0 12px}
.field-select::after{content:"";position:absolute;right:0;top:0;width:25px;height:23px;border-left:1px solid #ddd}
.caret{left:824px;top:742px;border:5px solid transparent;border-top-color:#555}
.submit{left:658px;top:846px;width:145px;height:22px;background:#111;color:var(--white);font-family:"Hind",sans-serif;font-weight:600;font-size:10.5px;text-align:center;line-height:23px}

/* footer */
.footer{left:0;top:924px;width:910px;height:230px;background:var(--dark)}
.footer-logo{left:68px;top:1010px;display:flex;align-items:center;gap:8px}
.footer-logo .logo-name{color:var(--lilac-text);font-size:20px;line-height:22px}
.footer-logo .logo-dot{background:var(--lilac-text)}
.foot-head{top:962px;font-family:"Hind",sans-serif;font-weight:600;font-size:12.5px;color:var(--white);padding-bottom:8px;border-bottom:1px solid #555}
.foot-list{top:1001px;font-size:10.4px;line-height:15.5px;color:#ddd;list-style:none}
.foot-contact{left:364px;top:1001px;font-size:10.4px;line-height:15px;color:#ddd}
.foot-contact .row{display:flex;gap:6px;margin-bottom:15px}
.map{left:558px;top:953px;width:287px;height:172px;background:linear-gradient(135deg,#e8e4d8,#f1ede2 40%,#d9dfe6);border:1px solid #555}
.bottom-bar{left:0;top:1154px;width:910px;height:24px;background:var(--purple-bright);color:var(--white);font-size:7.4px;font-weight:700;line-height:24px;padding-left:24px}
.bottom-social{left:857px;top:1159px;display:flex;gap:4px}
.bottom-social i{width:14px;height:14px;border-radius:50%;background:var(--white);display:block}
</style>
</head>
<body>
<div class="site">

  <header>
    <div class="abs header"></div>
    <div class="abs logo-box"><span class="logo-dot"></span><span class="logo-name">Bramble Ridge<br>Foot Care</span></div>
    <div class="abs top-tab">
      <svg width="16" height="16" viewBox="0 0 16 16"><circle cx="8" cy="8" r="7" fill="none" stroke="#fff" stroke-width="1.4"/><rect x="4" y="5.5" width="8" height="5.5" fill="none" stroke="#fff" stroke-width="1.1"/><path d="M4 5.5l4 3 4-3" fill="none" stroke="#fff" stroke-width="1.1"/></svg>
      info@brambleridgefootcare.com
      <span style="display:flex;gap:2px;margin-left:18px"><i class="circle-icon"></i><i class="circle-icon"></i></span>
    </div>
    <div class="abs contact-row">
      <span><svg width="21" height="21" viewBox="0 0 22 22"><circle cx="11" cy="11" r="10" fill="none" stroke="#fff" stroke-width="1.5"/><path d="M7.5 6.5c1-.6 1.6-.4 2 .5l.6 1.5c.2.6 0 1-.5 1.3-.3.2-.3.6-.1 1 .6 1 1.3 1.7 2.3 2.3.4.2.8.2 1-.1.3-.5.7-.7 1.3-.5l1.5.6c.9.4 1.1 1 .5 2-1 1.5-3.2 1.2-5.6-1.2S6 7.5 7.5 6.5z" fill="#fff"/></svg>1300 555 012</span>
      <span><svg width="21" height="21" viewBox="0 0 22 22"><circle cx="11" cy="11" r="10" fill="none" stroke="#fff" stroke-width="1.5"/><path d="M11 5a4 4 0 0 1 4 4c0 3-4 7.5-4 7.5S7 12 7 9a4 4 0 0 1 4-4z" fill="none" stroke="#fff" stroke-width="1.4"/><circle cx="11" cy="9" r="1.4" fill="#fff"/></svg>Suite 42 / 118 Ridgeway Street Melbourne 3000</span>
    </div>
    <nav class="abs nav">
      <a class="active" style="left:346px">HOME</a>
      <a style="left:428px">ABOUT US</a>
      <a style="left:533px">SERVICES &#8964;</a>
      <a style="left:642px">CONTACT</a>
      <a style="left:744px">BLOG</a>
    </nav>
  </header>

  <section class="hero">
    <div class="abs hero-panel p1" role="img" aria-label="Photo of a runner's foot with the heel bones highlighted"></div>
    <div class="abs hero-panel p2" role="img" aria-label="Photo of runners' legs on a road during a race"></div>
    <div class="abs hero-panel p3" role="img" aria-label="Photo of a runner at sunset on a waterfront path"></div>
    <div class="abs hero-panel p4" role="img" aria-label="Photo of a runner's leg and running shoe"></div>

    <div class="abs services-card">
      <div class="services-title">OUR SERVICES</div>
      <div class="card-text" style="top:142px">At Bramble Ridge Foot Care, we provide general treatments including; Nails, Corns, Callus, Warts, Skin Disorders, Heel Pain, Heel Spurs, Arch Pain-Plantar Fasciitis, Ankle Pain, Shin Splints, Knee Paint, Bunions, Hammestoes and Toe Deformities</div>
      <div class="card-divider"></div>
      <div class="card-text" style="top:262px"><div class="card-head">Specialised Treatments</div>Our specialised treatments including; Diabetic Management, Nail Surgery, Biomechanical Assessment, Gait Analysis, and Orthotic Therapy.</div>
    </div>
    <div class="abs treat-band">General Treatments</div>
    <div class="abs treat-photo" role="img" aria-label="Photo of gloved hands examining a patient's foot"></div>
  </section>

  <section class="welcome">
    <h1 class="abs welcome-title">Welcome to <span>Bramble Ridge Foot Care</span></h1>
    <div class="abs rule" style="left:44px;width:215px"></div>
    <div class="abs rule-dot"></div>
    <div class="abs rule" style="left:295px;width:215px"></div>
    <div class="abs intro">
      <p>Bramble Ridge Foot Care is a Podiatry clinic in the heart of Melbourne CBD. We are located between Elm &amp; Carver Streets in the Harbourview Business Centre.</p>
      <p>Our podiatrists are fully qualified health professionals who are able to diagnose, treat, manage or help to prevent all medical conditions that affect the feet and lower limb.</p>
      <p>We provide General Podiatry Treatment and some Specialised Services in relation to various foot conditions, including Sports Injuries, Orthotic Therapy and Nail Surgery.</p>
      <p>For Appointments or Enquiries please call us on <b>1300 555 012</b> or<br>email: <b>info@brambleridgefootcare.com</b></p>
    </div>
    <div class="abs btn btn-services">
      <svg width="24" height="20" viewBox="0 0 24 20"><path d="M2 10l7 7L22 3" fill="none" stroke="#9fb8ff" stroke-width="3.5"/></svg>OUR SERVICES
    </div>
    <div class="abs btn btn-videos">
      <svg width="22" height="22" viewBox="0 0 22 22"><circle cx="11" cy="11" r="11" fill="#7a6ad0"/><path d="M9 6.5l6 4.5-6 4.5z" fill="#3d2a9a"/></svg>TREATMENT VIDEOS
    </div>
  </section>

  <section class="appointment">
    <div class="abs form-shell"></div>
    <div class="abs form-cap"></div>
    <div class="abs form-head">Schedule an Appointment</div>

    <div class="abs field-icon" style="top:636px"><svg width="12" height="14" viewBox="0 0 12 14"><circle cx="6" cy="4" r="3.2" fill="#555"/><path d="M0 14c0-4 2.5-6 6-6s6 2 6 6z" fill="#555"/></svg></div>
    <div class="abs field" style="top:636px">NAME</div>
    <div class="abs field-icon" style="top:668px"><svg width="13" height="13" viewBox="0 0 13 13"><path d="M2 1c1-.6 1.6-.4 2 .5l.7 1.6c.2.6 0 1-.5 1.3-.3.2-.3.6-.1 1 .6 1 1.3 1.7 2.3 2.3.4.2.8.2 1-.1.3-.5.7-.7 1.3-.5l1.6.7c.9.4 1.1 1 .5 2-1 1.5-3.5 1.2-6-1.2S.5 2 2 1z" fill="#555"/></svg></div>
    <div class="abs field" style="top:668px">MOBILE PHONE</div>
    <div class="abs field-icon" style="top:700px;font-size:14px;color:#555;font-weight:700">@</div>
    <div class="abs field" style="top:700px">EMAIL</div>
    <div class="abs field-icon" style="top:732px"><svg width="10" height="14" viewBox="0 0 10 14"><rect x="1" y="1" width="8" height="12" rx="3" fill="#555"/></svg></div>
    <div class="abs field field-select" style="top:732px">INTERESTED IN</div>
    <div class="abs caret"></div>
    <div class="abs field-icon" style="top:764px"><svg width="14" height="11" viewBox="0 0 14 11"><rect x=".5" y=".5" width="13" height="10" fill="none" stroke="#555"/><path d="M.5 .5l6.5 5.5 6.5-5.5M.5 10.5l5-4.5M13.5 10.5l-5-4.5" fill="none" stroke="#555"/></svg></div>
    <div class="abs field" style="top:764px;height:75px">MESSAGE</div>
    <div class="abs submit">SUBMIT</div>
  </section>

  <footer>
    <div class="abs footer"></div>
    <div class="abs footer-logo"><span class="logo-dot"></span><span class="logo-name">Bramble Ridge<br>Foot Care</span></div>

    <div class="abs foot-head" style="left:234px;width:75px">QUICK LINKS</div>
    <ul class="abs foot-list" style="left:234px">
      <li>Home</li><li>About Us</li><li>Services</li><li>Contact Us</li><li>Blog</li>
    </ul>

    <div class="abs foot-head" style="left:354px;width:162px">CONTACT</div>
    <div class="abs foot-contact">
      <div class="row"><svg width="8" height="11" viewBox="0 0 8 11"><path d="M4 0a4 4 0 0 1 4 4c0 2.5-4 7-4 7S0 6.5 0 4a4 4 0 0 1 4-4z" fill="#5a4fc7"/></svg><span>Bramble Ridge Foot Care<br>Suite 42<br>118 Ridgeway Street<br>Melbourne 3000</span></div>
      <div class="row"><svg width="11" height="11" viewBox="0 0 13 13"><path d="M2 1c1-.6 1.6-.4 2 .5l.7 1.6c.2.6 0 1-.5 1.3-.3.2-.3.6-.1 1 .6 1 1.3 1.7 2.3 2.3.4.2.8.2 1-.1.3-.5.7-.7 1.3-.5l1.6.7c.9.4 1.1 1 .5 2-1 1.5-3.5 1.2-6-1.2S.5 2 2 1z" fill="#5a4fc7"/></svg><span>1300 555 012</span></div>
      <div class="row" style="margin-top:16px"><svg width="11" height="9" viewBox="0 0 11 9"><rect width="11" height="9" fill="#5a4fc7"/></svg><span>info@brambleridgefootcare.com</span></div>
    </div>

    <div class="abs map" role="img" aria-label="Street map of central Melbourne showing the clinic location"></div>

    <div class="abs bottom-bar">COPYRIGHT &copy; 2016 BRAMBLE RIDGE FOOT CARE. ALL RIGHTS RESERVED.</div>
    <div class="abs bottom-social"><i></i><i></i></div>
  </footer>

</div>
</body>
</html>
```